POP/ROCK artist: CD Cover Design Project

IF U LOVE MUSIC AND ALBUM COVER ART THEN PLEASE PARTICIPATE IN MY PROJECT AND HAVE A GREAT TIME DESIGNING SOMETHING UNIQUE AND EXCITING!!!!
Hi, my name is tovo, a pop/rock artist living in Europe. i just finished recording a fun dance song, called SPINNIN WILD HEARTS, with a successful Brightfield Records producer in Europe and I just put the finishing touches on the music video shot in LA. Now i'm going to release the song and video with PulsaWave. It's going to go out to about 750 stores, including SongCrate, tunebox and all the other biggies as well as a load of smaller ones.
I need a great looking CD cover design that i can plaster everywhere . . . and i really mean everywhere i can.
As per PulsaWave' specs, the cover art MUST BE 1500 x 1500 pixels. It cannot be blurry or pixilated and must be perfectly square.
I've uploaded some pics for you to choose from but you can use whichever one(s) you like . . . or none of them if you prefer, according to your inspiration. Just let me know if you want other pics and i can upload others.
Updates
Hey there,
Hey there,
Hi again, all,
Hey there,
Hi there, designers!
Hello everybody,
Target Market(s)
Modern pop/rock radio listeners of Kestrel Radio, ZPX, etc.
Please click on the following link to see the music video and hear the song:
http://www.clipvault.example/watch?v=Qr7tLm2Wd9a
Also, i have various pics and photos i can upload . . . just tell me what you need!!!!!
Requirements
Must have
- As per PulsaWave' specs, the cover art MUST BE 1500 x 1500 pixels. It cannot be blurry or pixilated and must be perfectly square.
My artist name, tovo, and the song title, Spinnin Wild Hearts, must be on the cover art.
The destination for your design is online music stores like SongCrate. So the dimensions will be VERY SMALL The actual size seen by the public will be about 1.5 cm x 1.5 cm! (Please have a look at the SongCrate store to see the actual size people will view the designs in.)
This means that your designs have to be clearly communicated at that size. The title of the song (spinnin wild hearts) and my artist name (tovo) have to be large enough to read and whatever idea you're going for has to be easily understood.
Nice to have
- It should look totally modern and pop/rock, hip and cool. It's up to you and your design magic to do whatever you think it takes.
Should not have
- Website and e-mail addresses CANNOT be included anywhere on cover art.

```html
<!DOCTYPE html>
<html lang="en">
<head>
<meta charset="utf-8">
<title>Spinnin Wild Hearts – tovo</title>
<link rel="stylesheet" href="https://fonts.googleapis.com/css2?family=Exo+2:wght@400;500&display=swap">
<style>
  :root {
    --teal: #3bb3a6;
    --orange: #f0892a;
    --gold: #d6a81c;
    --magenta: #d4127a;
    --amber: #c4740f;
    --band-edge: #3a2a14;
    --earth-dark: #5e4626;
    --earth-light: #b8a27a;
    --hatch-ground: #7a6038;
    --hatch-line: #f4efe4;
    --silhouette: #0d0d0d;
    --foliage: #20170c;
    --ink: #000000;
    --paper: #ffffff;
  }
  html, body {
    margin: 0;
    padding: 0;
    width: 1200px;
    height: 1200px;
    overflow: hidden;
    background: var(--paper);
  }
  .cover {
    position: relative;
    width: 1200px;
    height: 1200px;
    overflow: hidden;
    font-family: "Exo 2", "Helvetica Neue", Arial, sans-serif;
  }
  .cover-art {
    position: absolute;
    inset: 0;
    width: 1200px;
    height: 1200px;
  }
  .title-panel {
    position: absolute;
    top: 0;
    right: 0;
    width: 590px;
    height: 390px;
    background: var(--ink);
  }
  .song-title {
    position: absolute;
    top: 40px;
    left: 40px;
    margin: 0;
    color: var(--paper);
    font-weight: 400;
    font-size: 118px;
    line-height: 112px;
    letter-spacing: 1px;
  }
  .song-title span { display: block; }
  .artist-tag {
    position: absolute;
    right: 40px;
    top: 900px;
    width: 240px;
    height: 124px;
    margin: 0;
    background: var(--ink);
    color: var(--paper);
    font-weight: 500;
    font-size: 88px;
    line-height: 118px;
    text-align: center;
  }
</style>
</head>
<body>
  <main class="cover">
    <svg class="cover-art" viewBox="0 0 1200 1200" xmlns="http://www.w3.org/2000/svg">
      <defs>
        <linearGradient id="ground-gradient" x1="1" y1="0" x2="0" y2="1">
          <stop offset="0" stop-color="var(--earth-dark)"/>
          <stop offset="1" stop-color="var(--earth-light)"/>
        </linearGradient>
        <pattern id="pavement-lines" patternUnits="userSpaceOnUse" width="14" height="14" patternTransform="rotate(-35)">
          <rect width="14" height="14" fill="var(--hatch-ground)"/>
          <rect width="14" height="3" fill="var(--hatch-line)"/>
        </pattern>
        <radialGradient id="performer-shade" cx="0.5" cy="0.5" r="0.5">
          <stop offset="0" stop-color="var(--silhouette)" stop-opacity="0.95"/>
          <stop offset="0.6" stop-color="var(--silhouette)" stop-opacity="0.8"/>
          <stop offset="1" stop-color="var(--silhouette)" stop-opacity="0"/>
        </radialGradient>
        <radialGradient id="foliage-shade" cx="0.5" cy="0.5" r="0.5">
          <stop offset="0" stop-color="var(--foliage)" stop-opacity="0.95"/>
          <stop offset="0.6" stop-color="var(--foliage)" stop-opacity="0.75"/>
          <stop offset="1" stop-color="var(--foliage)" stop-opacity="0"/>
        </radialGradient>
      </defs>

      <rect class="ground" width="1200" height="1200" fill="url(#ground-gradient)"/>

      <polygon class="pavement" points="0,0 1200,0 1200,535 250,1200 0,1200" fill="url(#pavement-lines)"/>

      <polygon class="band band-amber" points="0,0 1200,0 1200,60 0,900" fill="var(--amber)"/>
      <polygon class="band band-magenta" points="0,0 1114,0 0,780" fill="var(--magenta)"/>
      <polygon class="band band-gold" points="0,0 914,0 0,640" fill="var(--gold)"/>
      <polygon class="band band-orange" points="0,0 671,0 0,470" fill="var(--orange)"/>
      <polygon class="band band-teal" points="0,0 329,0 0,230" fill="var(--teal)"/>
      <line class="band-edge" x1="0" y1="906" x2="1294" y2="0" stroke="var(--band-edge)" stroke-width="12"/>

      <ellipse class="street-trees" role="img" aria-label="Black silhouette of street trees and shrubs"
               cx="900" cy="560" rx="360" ry="400" fill="url(#foliage-shade)"/>

      <ellipse class="performer" role="img" aria-label="Black silhouette of a guitarist standing on the street"
               cx="260" cy="620" rx="200" ry="500" fill="url(#performer-shade)"/>
    </svg>

    <div class="title-panel">
      <h1 class="song-title"><span>SPINNIN</span><span>WILD</span><span>HEARTS</span></h1>
    </div>
    <p class="artist-tag">tovo</p>
  </main>
</body>
</html>
```